Tawny Bites menu + business card design

I want a menu design for my Food Truck.

I have attached the logo for it and my sliders will have different colors such as ( Black sliders, Red sliders and normal color) a picture will illustrates what I mean.

The menu should include:

Sliders:

Tawny Bite Single

Tawny Bites Meal

Fries:

Tawny Fries

Drinks:
Tawny Mojito

Water

BrisaPop

Desserts:

Charcoal cake

Target Market(s)

All

Industry/Entity Type

Business

Contact Information for Business Card

My theme is black and yellow like my logo

Colors

Designer to choose colors to be used in the design.

Requirements
Must have
• WhatsApp logo and the number for it is : +966507392048 " please dont squeeze the numbers".
• Instagram logo and my account is: TawnyBites
• Snapchat logo and my account is: TawnyBites
• Email logo and my email is: TheTawnyBites@postvale.com
Nice to have
• Circle design of the whole business card but it is not a must
• i will attach a picture.

```html
<!DOCTYPE html>
<html lang="en">
<head>
<meta charset="UTF-8">
<title>Tawny Bites – Circle Business Card</title>
<link rel="stylesheet" href="https://fonts.googleapis.com/css2?family=Poppins:wght@600;800&display=swap">
<style>
  :root {
    --backdrop: #2e2e2e;
    --card-light: #fbc21a;
    --card-mid: #f2a40a;
    --card-deep: #e48800;
    --ink-white: #ffffff;
    --ink-black: #141414;
  }
  html, body {
    margin: 0;
    padding: 0;
    width: 1200px;
    height: 873px;
    overflow: hidden;
    background: var(--backdrop);
  }
  .canvas {
    width: 1200px;
    height: 873px;
    display: block;
  }
  .contact-text {
    font-family: "Poppins", sans-serif;
    font-weight: 600;
    font-size: 19px;
    fill: var(--ink-white);
  }
  .contact-text--phone {
    font-size: 21px;
    letter-spacing: 1px;
  }
  .brand-name {
    font-family: "Poppins", sans-serif;
    font-weight: 800;
    font-size: 46px;
    fill: var(--ink-black);
    letter-spacing: 1px;
  }
  .icon-stroke {
    fill: none;
    stroke: var(--ink-white);
    stroke-width: 3;
    stroke-linejoin: round;
    stroke-linecap: round;
  }
</style>
</head>
<body>
<svg class="canvas" viewBox="0 0 1200 873" xmlns="http://www.w3.org/2000/svg">
  <defs>
    <radialGradient id="card-fill" cx="42%" cy="30%" r="75%">
      <stop offset="0%" stop-color="var(--card-light)"/>
      <stop offset="55%" stop-color="var(--card-mid)"/>
      <stop offset="100%" stop-color="var(--card-deep)"/>
    </radialGradient>
    <path id="arc-top" d="M 400,436 A 200 200 0 0 1 800,436"/>
    <path id="arc-bottom" d="M 395,436 A 205 205 0 0 0 805,436"/>
    <path id="arc-left" d="M 422,306 A 220 220 0 0 0 422,566"/>
    <path id="arc-right" d="M 778,566 A 220 220 0 0 0 778,306"/>
  </defs>

  <g class="business-card">
    <circle class="card-disc" cx="600" cy="436" r="240" fill="url(#card-fill)"/>

    <g class="brand-mark">
      <circle class="brand-dot" cx="600" cy="372" r="26" fill="var(--ink-black)"/>
      <text class="brand-name" x="600" y="444" text-anchor="middle">TAWNY</text>
      <text class="brand-name" x="600" y="494" text-anchor="middle">BITES</text>
    </g>

    <g class="contact-phone">
      <text class="contact-text contact-text--phone">
        <textPath href="#arc-top" startOffset="56%" text-anchor="middle">+966507392048</textPath>
      </text>
      <circle class="icon-stroke" cx="738" cy="284" r="12"/>
    </g>

    <g class="contact-instagram">
      <text class="contact-text">
        <textPath href="#arc-left" startOffset="55%" text-anchor="middle">TawnyBites</textPath>
      </text>
      <circle class="icon-stroke" cx="428" cy="304" r="12"/>
    </g>

    <g class="contact-snapchat">
      <text class="contact-text">
        <textPath href="#arc-right" startOffset="58%" text-anchor="middle">TawnyBites</textPath>
      </text>
      <circle class="icon-stroke" cx="784" cy="540" r="12"/>
    </g>

    <g class="contact-email">
      <text class="contact-text">
        <textPath href="#arc-bottom" startOffset="55%" text-anchor="middle">TheTawnyBites@postvale.com</textPath>
      </text>
      <g class="icon-envelope" transform="translate(462 566) rotate(40)">
        <rect class="icon-stroke" x="-15" y="-10" width="30" height="20" rx="2"/>
        <polyline class="icon-stroke" points="-15,-10 0,2 15,-10"/>
      </g>
    </g>
  </g>
</svg>
</body>
</html>
```